Veltharon Partner Needed Design for EKR Management Web App

We need a web app design for a new cloud based software called "Pruncely QMS". This software will be used by enterprises with EKR standards, and does manages audit (for both internal and external).
The application will be used to keep track of the tasks, activities and work process required to achieve the EKR process and audit completion.
It also provides a dashboard for different roles to access the required information and analysis at their fingertips. The standard screen currently available on the system has been provided in the attachment.
We need the design to be done based on a modern UI / UX, preferably flat UI based upon bootstrap.

Industry/Entity Type

Software

Coding

Coded - Design and coding required

Number of Pages Required

5+ page

Font styles to use
Sans Serif

Colors
f37122
ec1f27
9bcb3c

Requirements
Must have
• - Modern, Flat UI, based on Bootstrap.
• - Open for Suggestion on how to improve UX

```html
<!DOCTYPE html>
<html lang="en">
<head>
<meta charset="utf-8">
<title>Pruncely QMS – Request Details</title>
<link href="https://fonts.googleapis.com/css2?family=Roboto:wght@400;500;700&display=swap" rel="stylesheet">
<style>
:root{
  --red:#ec1f27;
  --orange:#f37122;
  --green:#9bcb3c;
  --grey-band:#ececec;
  --grey-head:#c4bcbc;
  --row-pink:#f7ecec;
  --row-light:#fbf6f6;
  --text:#555;
  --muted:#888;
  --dark-btn:#555;
  --line:#ddd;
}
*{box-sizing:border-box;margin:0;padding:0}
html,body{width:878px;height:1200px;overflow:hidden;background:#fff;font-family:"Roboto",Arial,sans-serif;color:var(--text)}
.page{position:relative;width:878px;height:1200px}
.topbar{position:absolute;top:0;left:0;width:878px;height:48px;border-bottom:1px solid #e4e4e4;background:#fff}
.brand{position:absolute;left:37px;top:13px;font-size:20px;font-weight:700;color:var(--orange);letter-spacing:1px}
.user{position:absolute;left:743px;top:0;width:88px;height:48px;border-left:1px solid #e4e4e4;border-right:1px solid #e4e4e4;font-size:12px;color:var(--muted);display:flex;align-items:center;padding-left:10px;gap:10px}
.caret{width:0;height:0;border-left:4px solid transparent;border-right:4px solid transparent;border-top:5px solid #777}
.gear{position:absolute;left:846px;top:17px}
.actionbar{position:absolute;top:48px;left:0;width:878px;height:32px;background:#f4f4f4}
.action{position:absolute;top:0;height:32px;font-size:8px;color:var(--muted);display:flex;align-items:center;gap:5px;padding:0 12px;border-left:1px solid #e2e2e2}
.navbar{position:absolute;top:80px;left:0;width:878px;height:42px;background:var(--grey-band);display:flex;align-items:center}
.nav-brand{margin-left:37px;color:var(--red);font-size:12px;width:92px}
.nav a{font-size:9.5px;color:var(--muted);text-decoration:none;margin-right:32px;letter-spacing:.3px;display:inline-flex;align-items:center;gap:4px}
.panel{position:absolute;left:37px;width:802px}
.panel-title{height:41px;display:flex;align-items:center;padding-left:14px;font-size:15px;color:#fff}
.panel-title.red{background:var(--red)}
.panel-title.grey{background:var(--grey-head)}
.form-row{display:flex;height:29.2px;align-items:center;font-size:9.8px}
.form-row:nth-child(odd){background:var(--row-pink)}
.form-row:nth-child(even){background:var(--row-light)}
.label{width:356px;text-align:right;padding-right:49px;border-right:1px solid #e8e0e0;height:100%;display:flex;align-items:center;justify-content:flex-end}
.value{padding-left:41px;display:flex;align-items:center;gap:8px}
.select{width:204px;height:15px;border:1px solid #ccc;background:#fff;font-size:8px;padding-left:9px;display:flex;align-items:center;position:relative;color:#555}
.select::after{content:"";position:absolute;right:0;top:0;width:16px;height:13px;background:#e6e6e6;border-left:1px solid #ccc}
.select::before{content:"";position:absolute;right:5px;top:5px;border-left:3px solid transparent;border-right:3px solid transparent;border-top:4px solid #888;z-index:1}
.date{width:70px;height:15px;border:1px solid #ccc;background:#fff;font-size:8px;padding-left:5px;display:flex;align-items:center}
.btn{position:absolute;height:26px;width:65px;color:#fff;font-size:11px;font-weight:700;display:flex;align-items:center;justify-content:center;letter-spacing:.5px}
.btn.green{background:var(--green)}
.btn.orange{background:var(--orange)}
.btn.dark{background:var(--dark-btn)}
.grid{position:absolute;left:37px;top:716px;width:803px;border-collapse:collapse;font-size:9.8px;table-layout:fixed}
.grid th{background:var(--red);color:#fff;font-weight:400;font-size:12px;height:40px;border-right:1px solid #f26;text-align:center}
.grid td{border-right:1px solid #e8e0e0;vertical-align:middle;line-height:19.5px;padding-left:20px}
.grid tr.r1 td{background:var(--row-pink);height:136px}
.grid tr.r2 td{background:var(--row-light);height:201px}
.grid td.clauses{font-size:9.3px;line-height:13px;padding-left:21px}
.grid td.edit{padding-left:0;text-align:center}
</style>
</head>
<body>
<div class="page">
  <header class="topbar">
    <div class="brand">PRUNCELY</div>
    <div class="user">Dara Venn <span class="caret"></span></div>
    <svg class="gear" width="14" height="14" viewBox="0 0 14 14" aria-hidden="true"><circle cx="7" cy="7" r="4.5" fill="none" stroke="#999" stroke-width="3" stroke-dasharray="2.2 1.3"/><circle cx="7" cy="7" r="3.2" fill="none" stroke="#999" stroke-width="2"/></svg>
  </header>
  <div class="actionbar">
    <div class="action" style="left:730px">SHARE <svg width="9" height="8" viewBox="0 0 9 8"><path d="M1 7 C1 3 4 2.5 6 2.5 V0.5 L9 3.5 L6 6.5 V4.5 C4 4.5 2 5 1 7Z" fill="#999"/></svg></div>
    <div class="action" style="left:798px">FOLLOW <svg width="8" height="8" viewBox="0 0 10 10"><path d="M5 0 L6.2 3.6 L10 3.6 L7 5.9 L8.1 9.5 L5 7.3 L1.9 9.5 L3 5.9 L0 3.6 L3.8 3.6Z" fill="#999"/></svg></div>
  </div>
  <nav class="navbar">
    <div class="nav-brand">Pruncely</div>
    <div class="nav">
      <a>Home</a><a>Quality Management <span class="caret"></span></a><a>Master Maintainance</a><a>About</a><a>Contact</a>
    </div>
  </nav>

  <section class="panel" style="top:156px">
    <div class="panel-title red">Request Details</div>
    <div class="rows">
      <div class="form-row"><div class="label">Date Request</div><div class="value">10/05/2015</div></div>
      <div class="form-row"><div class="label">Status</div><div class="value">Draft</div></div>
      <div class="form-row"><div class="label">Requestor</div><div class="value">DARA VENN</div></div>
      <div class="form-row"><div class="label">Dept/Section</div><div class="value">Supply chain / Quality &amp; Process Assurance</div></div>
      <div class="form-row"><div class="label">Job Title</div><div class="value">Executive Quality &amp; Process Assurance</div></div>
      <div class="form-row"><div class="label">* Standard</div><div class="value"><div class="select">EKR 9001</div></div></div>
      <div class="form-row"><div class="label">* Audit No</div><div class="value"><div class="select">EKR 9001/5/2015</div></div></div>
      <div class="form-row"><div class="label">* Date Plan</div><div class="value">From <div class="date">19/05/2015</div>
        <svg width="9" height="9" viewBox="0 0 9 9"><rect x="0.5" y="1.5" width="8" height="7" fill="none" stroke="#e23" /><rect x="0.5" y="1.5" width="8" height="2" fill="#e23"/></svg>
        <span style="margin-left:16px">To</span> <div class="date">22/05/2015</div>
        <svg width="9" height="9" viewBox="0 0 9 9"><rect x="0.5" y="1.5" width="8" height="7" fill="none" stroke="#e23" /><rect x="0.5" y="1.5" width="8" height="2" fill="#e23"/></svg></div></div>
    </div>
  </section>

  <section class="panel" style="top:462px;width:803px">
    <div class="panel-title grey">Lead Auditor(s) &amp; Auditor(s) *</div>
    <div class="rows">
      <div class="form-row"><div class="label">* Audit Section</div><div class="value"><div class="select">-SELECT-</div></div></div>
      <div class="form-row"><div class="label">* Audit Area</div><div class="value"><div class="select">-SELECT-</div></div></div>
      <div class="form-row"><div class="label">* Lead Auditor</div><div class="value"><div class="select">-SELECT-</div></div></div>
      <div class="form-row"><div class="label">* Auditor</div><div class="value"><div class="select">-SELECT-</div></div></div>
    </div>
  </section>

  <div class="btn green" style="left:311px;top:646px">ADD</div>
  <div class="btn orange" style="left:409px;top:646px">RESET</div>

  <table class="grid">
    <colgroup><col style="width:115px"><col style="width:126px"><col style="width:128px"><col style="width:112px"><col style="width:257px"><col style="width:65px"></colgroup>
    <thead><tr><th>Audit Section</th><th>Audit Area</th><th>Lead Auditor</th><th>Auditor</th><th>Clauses</th><th>Edit</th></tr></thead>
    <tbody>
      <tr class="r1"><td>Procurement &amp;<br>Planning</td><td>Purchasing</td><td>Mira Solt</td><td>Tobin Kade</td>
        <td class="clauses">4.2.1. General<br>4.2.3. Control of Documents<br>5.3. Quality Policy<br>6.2.2. Competence &amp; Training<br>7.4.1. Purchasing Process<br>7.4.2. Purchasing Information<br>7.4.3. verification of purchased product<br>7.5.1. Control of Production and&nbsp; Service Provision<br>8.4. Analysis of Data</td>
        <td class="edit"><svg width="30" height="12" viewBox="0 0 30 12"><rect x="1" y="1.5" width="10" height="9.5" fill="none" stroke="#f37122"/><rect x="1" y="1.5" width="10" height="2.5" fill="#f37122"/><path d="M3 6h1M6 6h1M9 6h0.5M3 8.5h1M6 8.5h1" stroke="#f37122"/><circle cx="24" cy="6" r="4.5" fill="#9bcb3c"/><path d="M22.3 4.3l3.4 3.4M25.7 4.3l-3.4 3.4" stroke="#fff" stroke-width="1.3"/></svg></td></tr>
      <tr class="r2"><td>Quality &amp; Process<br>Assurance</td><td>QA</td><td>Mira Solt</td><td>Tobin Kade</td>
        <td class="clauses">4.2.1. General<br>4.2.3. Control of Documents<br>5.3. Quality Policy<br>6.2.2. Competence &amp; Training<br>7.4.1. Purchasing Process<br>7.4.2. Purchasing Information<br>7.4.3. verification of purchased product<br>7.5.1. Control of Production and&nbsp; Service Provision<br>8.4. Analysis of Data<br>8.5.1. Continual Improvement<br>8.5.2. Corrective Action<br>8.4. Preventive Action</td>
        <td class="edit"><svg width="30" height="12" viewBox="0 0 30 12"><rect x="1" y="1.5" width="10" height="9.5" fill="none" stroke="#f37122"/><rect x="1" y="1.5" width="10" height="2.5" fill="#f37122"/><path d="M3 6h1M6 6h1M9 6h0.5M3 8.5h1M6 8.5h1" stroke="#f37122"/><circle cx="24" cy="6" r="4.5" fill="#9bcb3c"/><path d="M22.3 4.3l3.4 3.4M25.7 4.3l-3.4 3.4" stroke="#fff" stroke-width="1.3"/></svg></td></tr>
    </tbody>
  </table>

  <div class="btn green" style="left:260px;top:1122px">SAVE</div>
  <div class="btn dark" style="left:358px;top:1122px">DELETE</div>
  <div class="btn dark" style="left:455px;top:1122px">SUBMIT</div>
  <div class="btn dark" style="left:553px;top:1122px">BACK</div>
</div>
</body>
</html>
```